SEHLAN REAL ESTATE
شركة السهلان العقارية
Creative Brief
Simple
FAISAL ALQUDRANI
Real Estate Consultant & Developer
SAUDI ARABIA.JEDDAH
f_alqudrani@mailvesta.com
THE LOGO
Yasahiro17 Yasahiro17
YADESIGN YADESIGN

```html
<!DOCTYPE html>
<html lang="en">
<head>
<meta charset="utf-8">
<title>Sehlan Real Estate — Stationery</title>
<link href="https://fonts.googleapis.com/css2?family=Cinzel:wght@400;600&family=Noto+Naskh+Arabic:wght@500&display=swap" rel="stylesheet">
<style>
  :root {
    --brand-blue: #2b7bc0;
    --paper: #ffffff;
    --backdrop: #ffffff;
    --ink: #4a4f55;
    --shadow: rgba(0,0,0,0.18);
    --latin: 'Cinzel', serif;
    --arabic: 'Noto Naskh Arabic', serif;
  }
  * { box-sizing: border-box; margin: 0; padding: 0; }
  html, body { width: 1200px; height: 871px; overflow: hidden; background: var(--backdrop); }
  .canvas { position: relative; width: 1200px; height: 871px; }
  .sheet { position: absolute; background: var(--paper); box-shadow: 0 1px 4px var(--shadow); }
  .sheet--blue { background: var(--brand-blue); }

  .brand { display: flex; align-items: center; gap: 8px; color: var(--brand-blue); }
  .brand__mark { background: currentColor; flex: none; }
  .brand__text { display: flex; flex-direction: column; line-height: 1.1; }
  .brand__name { font-family: var(--latin); font-weight: 600; letter-spacing: 0.04em; }
  .brand__arabic { font-family: var(--arabic); font-weight: 500; }
  .brand--light { color: #fff; }

  .contact { font-family: var(--latin); color: var(--ink); line-height: 1.55; letter-spacing: 0.03em; }

  /* business card front */
  .card-front { left: 70px; top: 110px; width: 258px; height: 130px; }
  .card-front .brand { position: absolute; left: 20px; top: 22px; }
  .card-front .brand__mark { width: 14px; height: 14px; }
  .card-front .brand__name { font-size: 11px; }
  .card-front .brand__arabic { font-size: 10px; }
  .card-front .person { position: absolute; left: 20px; top: 88px; font-family: var(--latin); color: var(--ink); }
  .person__name { font-size: 7px; letter-spacing: 0.05em; }
  .person__role { font-size: 4.5px; margin-top: 2px; }
  .card-front .contact { position: absolute; left: 128px; top: 86px; font-size: 4.5px; }

  /* business card back */
  .card-back { left: 345px; top: 110px; width: 255px; height: 130px; display: flex; align-items: center; justify-content: center; }
  .card-back .brand__mark { width: 18px; height: 18px; }
  .card-back .brand__name { font-size: 13px; }
  .card-back .brand__arabic { font-size: 11px; }

  /* envelope front */
  .envelope { left: 70px; top: 278px; width: 530px; height: 240px; }
  .envelope .brand { position: absolute; left: 40px; top: 38px; }
  .envelope .brand__mark { width: 22px; height: 22px; }
  .envelope .brand__name { font-size: 16px; }
  .envelope .brand__arabic { font-size: 14px; }
  .envelope .contact { position: absolute; left: 40px; top: 162px; font-size: 8.5px; }

  /* envelope back */
  .envelope-back { left: 70px; top: 548px; width: 530px; height: 245px; overflow: hidden; }
  .envelope-back svg { position: absolute; inset: 0; }
  .envelope-back .brand { position: absolute; left: 50%; top: 128px; transform: translateX(-50%); }
  .envelope-back .brand__mark { width: 20px; height: 20px; }
  .envelope-back .brand__name { font-size: 15px; }
  .envelope-back .brand__arabic { font-size: 13px; }

  /* letterhead */
  .letterhead { left: 655px; top: 108px; width: 468px; height: 675px; }
  .letterhead .brand { position: absolute; left: 52px; top: 50px; }
  .letterhead .brand__mark { width: 18px; height: 18px; }
  .letterhead .brand__name { font-size: 12px; }
  .letterhead .brand__arabic { font-size: 10px; }
  .letterhead .contact { position: absolute; left: 318px; top: 56px; font-size: 6px; }
</style>
</head>
<body>
<main class="canvas">

  <section class="sheet card-front" aria-label="Business card front">
    <div class="brand">
      <span class="brand__mark"></span>
      <div class="brand__text">
        <span class="brand__name">SEHLAN REAL ESTATE</span>
        <span class="brand__arabic" dir="rtl">شركة السهلان العقارية</span>
      </div>
    </div>
    <div class="person">
      <p class="person__name">FAISAL ALQUDRANI</p>
      <p class="person__role">Real Estate Consultant &amp; Developer</p>
    </div>
    <div class="contact">
      <p>SAUDI ARABIA.JEDDAH</p>
      <p>+966500012345</p>
      <p>f_alqudrani@mailvesta.com</p>
    </div>
  </section>

  <section class="sheet sheet--blue card-back" aria-label="Business card back">
    <div class="brand brand--light">
      <span class="brand__mark"></span>
      <div class="brand__text">
        <span class="brand__name">SEHLAN REAL ESTATE</span>
        <span class="brand__arabic" dir="rtl">شركة السهلان العقارية</span>
      </div>
    </div>
  </section>

  <section class="sheet envelope" aria-label="Envelope front">
    <div class="brand">
      <span class="brand__mark"></span>
      <div class="brand__text">
        <span class="brand__name">SEHLAN REAL ESTATE</span>
        <span class="brand__arabic" dir="rtl">شركة السهلان العقارية</span>
      </div>
    </div>
    <div class="contact">
      <p>SAUDI ARABIA.JEDDAH</p>
      <p>+966500012345</p>
      <p>f_alqudrani@mailvesta.com</p>
    </div>
  </section>

  <section class="sheet sheet--blue envelope-back" aria-label="Envelope back">
    <svg width="530" height="245" viewBox="0 0 530 245" aria-hidden="true">
      <polyline points="0,0 235,105 295,105 530,0" fill="none" stroke="rgba(0,0,0,0.18)" stroke-width="1.5"/>
      <polyline points="0,245 230,112" fill="none" stroke="rgba(0,0,0,0.1)" stroke-width="1"/>
      <polyline points="530,245 300,112" fill="none" stroke="rgba(0,0,0,0.1)" stroke-width="1"/>
    </svg>
    <div class="brand brand--light">
      <span class="brand__mark"></span>
      <div class="brand__text">
        <span class="brand__name">SEHLAN REAL ESTATE</span>
        <span class="brand__arabic" dir="rtl">شركة السهلان العقارية</span>
      </div>
    </div>
  </section>

  <section class="sheet letterhead" aria-label="Letterhead">
    <div class="brand">
      <span class="brand__mark"></span>
      <div class="brand__text">
        <span class="brand__name">SEHLAN REAL ESTATE</span>
        <span class="brand__arabic" dir="rtl">شركة السهلان العقارية</span>
      </div>
    </div>
    <div class="contact">
      <p>SAUDI ARABIA.JEDDAH</p>
      <p>+966500012345</p>
      <p>f_alqudrani@mailvesta.com</p>
    </div>
  </section>

</main>
</body>
</html>
```